New theme for existing wordpress site

We have an existing website at www.halvergatecw.com which uses wordpress. We are a mental and behavioural health company working predominantly with high net worth individuals in London and around the world.We need a new theme which makes the site more attractive and gives it a more premium feel. We would like to explore two possible concepts. Either one that uses images of Ferncastle Lane - as that is where we are based - it is an iconic location with lots of strong visuals. Or one which uses portraits of people. People are key to the work we do. Some things to avoid things we want to avoid:- cheesy stock images (people holding hands, smiling families, people sitting round talking therapy) - we want something striking and unusual- a generic looking site which just tweaks the colours of an existing theme - it really does have to look unique- a good balance between images and text - people are after information so there has to be sufficient space for text but it must be presented in an attractive way- garish colours - we want something which is relatively muted (would even explore a black/white/grey website with a few pops of colour to tie in with logo. No orange please.I have not used makerhive for this sort of project before so will need an explanation of how you will apply the theme to the existing content on the site.Feel free to use the HCW logo for colour and font inspiration. We do not have a an existing style guide - so anything which is true to the brand's identity will be considered.Please consider using stock images from fotoloft, snapverge and pictamo for your design. If you want images of Ferncastle Lane these can be supplied.

Target Market(s)

Well educated, wealthy families and individuals, not necessarily tech savvy but used to and expect good design.

Industry/Entity Type

Health And Wellness

Font styles to use
Sans Serif

Colors

Designer to choose colors to be used in the design.

Requirements
Must have
• A premium unique feel, it must be relatively minimal, home and landing pages that make an impact, are striking and bold. Must have strong royalty free imagery. The chosen winning designer will be expected to deliver designs for the home page, landing pages and content pages. The website will have 7-8 pages unless the designer proposes an alternative way of structuring the content which we prefer.
Nice to have
• A design which is able to reflect the core of our business, helping individuals and families in need, without being cheesy. A video landing page could be cool.
• Should be calm, and cool.
• Be good to see a monochrome design with a pop of colour.
Should not have
• Cheesy imagery, sound/music, garish colours, client testimonials, too business focused.

```html
<!DOCTYPE html>
<html lang="en">
<head>
<meta charset="utf-8">
<title>Halvergate Behavioural Health</title>
<link href="https://fonts.googleapis.com/css2?family=Oswald:wght@300;400&family=Open+Sans:wght@400;600&display=swap" rel="stylesheet">
<style>
  :root {
    --ink: #ffffff;
    --shade-dark: #1c1c1c;
    --shade-mid: #4a4a4a;
    --shade-light: #a9a9a9;
    --sky: #cfcfcf;
  }
  * { margin: 0; padding: 0; box-sizing: border-box; }
  html, body { width: 1200px; height: 804px; overflow: hidden; background: var(--shade-dark); }
  .hero {
    position: relative;
    width: 1200px;
    height: 804px;
    overflow: hidden;
    color: var(--ink);
    font-family: 'Open Sans', sans-serif;
  }
  .hero-photo {
    position: absolute;
    inset: 0;
    background:
      radial-gradient(ellipse 420px 260px at 640px 90px, var(--sky) 0%, rgba(180,180,180,0.6) 45%, transparent 100%),
      radial-gradient(ellipse 260px 520px at 600px 640px, #262626 0%, transparent 80%),
      linear-gradient(90deg, #2a2a2a 0%, #3c3c3c 22%, #6d6d6d 45%, #5a5a5a 60%, #2f2f2f 82%, #1f1f1f 100%);
  }
  .hero-photo::after {
    content: "";
    position: absolute;
    inset: 0;
    background: linear-gradient(180deg, rgba(0,0,0,0) 40%, rgba(0,0,0,0.35) 100%);
  }
  .brand {
    position: absolute;
    left: 111px;
    top: 34px;
    width: 224px;
    text-align: center;
    font-family: 'Oswald', sans-serif;
    font-weight: 400;
    color: var(--ink);
  }
  .brand-mark {
    display: block;
    width: 104px;
    height: 104px;
    margin: 0 auto 16px;
    border-radius: 50%;
    border: 3px solid var(--ink);
  }
  .brand-name { font-size: 40px; line-height: 1; letter-spacing: 0.5px; }
  .brand-tag { font-size: 17px; line-height: 1.5; letter-spacing: 1.5px; margin-top: 6px; }
  .main-nav {
    position: absolute;
    left: 1073px;
    top: 80px;
    list-style: none;
    font-family: 'Oswald', sans-serif;
    font-weight: 300;
    font-size: 22px;
  }
  .main-nav li { height: 94.5px; line-height: 32px; }
  .headline {
    position: absolute;
    left: 0; right: 0;
    top: 395px;
    text-align: center;
    font-family: 'Oswald', sans-serif;
    font-weight: 300;
    font-size: 78px;
    letter-spacing: 17px;
    line-height: 1.2;
    padding-left: 17px;
  }
  .play-button {
    position: absolute;
    left: 565px;
    top: 540px;
    width: 70px;
    height: 70px;
  }
  .contact-line {
    position: absolute;
    left: 0; right: 0;
    top: 692px;
    display: flex;
    justify-content: center;
    align-items: center;
    gap: 14px;
    font-weight: 600;
    font-size: 19px;
  }
  .contact-item { display: flex; align-items: center; gap: 10px; }
  .contact-divider { font-weight: 400; padding: 0 6px; }
  .copyright {
    position: absolute;
    left: 0; right: 0;
    top: 748px;
    text-align: center;
    font-size: 14px;
    font-weight: 400;
  }
</style>
</head>
<body>
<main class="hero">
  <div class="hero-photo" role="img" aria-label="Black and white photograph of a hiker with a backpack looking out over a forested mountain valley"></div>

  <div class="brand">
    <span class="brand-mark"></span>
    <div class="brand-name">HALVERGATE</div>
    <div class="brand-tag">Behavioural Health</div>
  </div>

  <ul class="main-nav">
    <li>ABOUT</li>
    <li>SERVICES</li>
    <li>TEAM</li>
    <li>CONTACT</li>
  </ul>

  <h1 class="headline">BEHAVIOURAL HEALTH</h1>

  <svg class="play-button" viewBox="0 0 70 70" aria-label="Play video">
    <circle cx="35" cy="35" r="33.5" fill="none" stroke="#fff" stroke-width="2"/>
    <path d="M26 20 L51 35 L26 50 Z" fill="#fff"/>
  </svg>

  <div class="contact-line">
    <span class="contact-item">
      <svg width="19" height="15" viewBox="0 0 19 15" aria-hidden="true">
        <rect x="0" y="0" width="19" height="15" rx="2" fill="#fff"/>
        <path d="M1 2 L9.5 8.5 L18 2" fill="none" stroke="#2a2a2a" stroke-width="1.6"/>
      </svg>
      enquiries@halvergatecw.com
    </span>
    <span class="contact-divider">|</span>
    <span class="contact-item">
      <svg width="16" height="16" viewBox="0 0 24 24" aria-hidden="true">
        <path fill="#fff" d="M6.6 10.8c1.4 2.8 3.8 5.1 6.6 6.6l2.2-2.2c.3-.3.7-.4 1-.2 1.1.4 2.3.6 3.6.6.6 0 1 .4 1 1V20c0 .6-.4 1-1 1C10.6 21 3 13.4 3 4c0-.6.4-1 1-1h3.5c.6 0 1 .4 1 1 0 1.3.2 2.5.6 3.6.1.3 0 .7-.2 1z"/>
      </svg>
      020 7946 0381
    </span>
  </div>

  <p class="copyright">Halvergate Behavioural Health © 2019 All rights reserved.</p>
</main>
</body>
</html>
```